To create a visually compelling, mission-aligned report that:
Presents research findings on pastoral succession and financial literacy in Lebanon.
Communicates funding opportunities to individual donors, churches, and Christian foundations.
Builds trust and credibility with potential partners.
Inspires support and engagement through storytelling, impact framing, and visual clarity.

The deliverable should be a polished report of approximately 10 - 14 pages. The report should have page breaks that are reflected in the PDF. The headings should be very clear and bold. We'd like to see colors of blues and greens and whites. We want the report to be slightly edgy and bold, but still professional and clear.

```html
<!DOCTYPE html>
<html lang="en">
<head>
<meta charset="utf-8">
<title>Leadership and Financial Health of Pastors in Lebanon – Report Pages</title>
<link href="https://fonts.googleapis.com/css2?family=Poppins:wght@400;500;600;700;800&display=swap" rel="stylesheet">
<style>
  :root{
    --navy:#032f42;
    --navy-text:#0b2a3a;
    --teal:#0d5b78;
    --teal-soft:#1d6f8c;
    --backdrop:#bdbdbd;
    --white:#ffffff;
    --mist:#eceff1;
    --ink:#1c2a33;
  }
  *{margin:0;padding:0;box-sizing:border-box;}
  html,body{width:974px;height:1200px;overflow:hidden;}
  body{background:var(--backdrop);font-family:"Poppins",sans-serif;color:var(--ink);position:relative;}

  .page{position:absolute;width:387px;height:501px;background:var(--white);overflow:hidden;}
  .page--cover{left:79px;top:72px;}
  .page--summary{left:513px;top:72px;}
  .page--findings{left:80px;top:632px;}
  .page--contact{left:516px;top:632px;}

  .cover-art{position:absolute;inset:0;width:100%;height:100%;}

  .brand{position:absolute;display:flex;align-items:center;gap:5px;font-family:"Poppins",sans-serif;font-weight:800;color:var(--navy-text);letter-spacing:2px;}
  .brand__dot{width:15px;height:15px;border-radius:50%;background:var(--navy-text);flex:none;}
  .brand--cover{left:39px;top:82px;font-size:22px;}
  .brand--cover .brand__dot{width:20px;height:20px;}
  .brand--contact{left:39px;top:418px;font-size:20px;}
  .brand--contact .brand__dot{width:18px;height:18px;}

  .cover-title{position:absolute;left:39px;top:180px;font-weight:700;font-size:24px;line-height:29px;color:var(--navy-text);letter-spacing:.2px;}
  .cover-subtitle{position:absolute;left:39px;top:243px;font-weight:500;font-size:13.5px;color:var(--navy-text);letter-spacing:.3px;}
  .cover-rule{position:absolute;left:40px;top:267px;width:24px;height:3px;background:var(--teal);border-radius:2px;}
  .cover-year{position:absolute;left:39px;top:405px;font-weight:700;font-size:14px;color:var(--navy-text);}
  .cover-byline{position:absolute;left:39px;top:430px;font-weight:500;font-size:9.5px;color:var(--teal);letter-spacing:.3px;}

  .running-head{position:absolute;left:0;right:0;display:flex;align-items:center;}
  .running-head__line{height:1px;background:var(--navy-text);flex:1;}
  .running-head__dot{width:3px;height:3px;border-radius:50%;background:var(--navy-text);margin:0 3px;flex:none;}
  .running-head__pill{flex:none;background:var(--teal);color:var(--white);font-size:5.2px;font-weight:500;padding:2.5px 5px;border-radius:6px;letter-spacing:.1px;white-space:nowrap;}
  .page--summary .running-head{top:39px;}
  .page--summary .running-head__line:first-child{flex:0 0 56px;}
  .page--findings .running-head{top:40px;}
  .page--findings .running-head__line:first-child{flex:0 0 56px;}

  .page-foot{position:absolute;left:0;right:0;top:456px;display:flex;align-items:center;}
  .page-foot__line{height:1px;background:var(--navy-text);flex:1;}
  .page-foot__line--lead{flex:0 0 40px;}
  .page-foot__brand{display:flex;align-items:center;gap:3px;font-weight:800;font-size:9px;color:var(--navy-text);letter-spacing:1.2px;margin:0 4px;}
  .page-foot__brand span{width:10px;height:10px;border-radius:50%;background:var(--navy-text);}
  .page-foot__dot{width:3px;height:3px;border-radius:50%;background:var(--navy-text);margin:0 3px;flex:none;}
  .page-foot__num{width:13px;height:13px;border-radius:50%;background:var(--navy);color:var(--white);font-size:5.5px;font-weight:500;display:flex;align-items:center;justify-content:center;flex:none;}
  .page-foot__line--tail{flex:0 0 30px;}

  .section-title{position:absolute;left:39px;top:76px;font-weight:800;font-size:27px;color:var(--navy-text);letter-spacing:-.3px;}
  .subhead{font-weight:600;font-size:9.4px;color:var(--navy-text);}
  .body-text{font-size:7.1px;line-height:9.5px;text-align:justify;color:var(--ink);}

  .summary-purpose{position:absolute;left:39px;top:121px;}
  .summary-icon{position:absolute;left:70px;top:143px;width:60px;height:62px;background:radial-gradient(circle at 50% 40%,#2c4a5a,var(--navy-text));border-radius:30px 30px 8px 8px;}
  .summary-intro{position:absolute;left:196px;top:123px;width:152px;}
  .summary-method{position:absolute;left:40px;top:220px;width:309px;}
  .summary-findings{position:absolute;left:39px;top:299px;width:309px;}

  .findings-list{list-style:none;margin-top:6px;}
  .findings-list li{position:relative;padding-left:10px;margin-bottom:9px;font-size:7.1px;line-height:9.5px;text-align:justify;}
  .findings-list li::before{content:"";position:absolute;left:2px;top:3.6px;width:2.4px;height:2.4px;border-radius:50%;background:var(--ink);}
  .findings-list--tight li{margin-bottom:5px;}

  .findings-money{position:absolute;left:39px;top:82px;width:309px;}
  .findings-training{position:absolute;left:39px;top:181px;width:309px;}

  .action-band{position:absolute;left:0;top:250px;width:387px;height:191px;background:var(--navy);color:var(--white);}
  .action-band__title{position:absolute;left:41px;top:45px;font-weight:800;font-size:26px;line-height:31px;letter-spacing:-.2px;}
  .action-band__lede{position:absolute;left:172px;top:19px;width:176px;color:var(--white);}
  .action-band__invite{position:absolute;left:39px;top:141px;width:309px;color:var(--white);}

  .contact-title{position:absolute;left:38px;top:138px;font-weight:700;font-size:24px;color:var(--navy-text);}
  .contact-list{position:absolute;left:38px;top:185px;list-style:none;}
  .contact-list li{display:flex;align-items:center;gap:10px;height:23px;font-size:15px;color:var(--navy-text);}
  .contact-list svg{width:15px;height:15px;flex:none;}
</style>
</head>
<body>

<!-- Cover -->
<section class="page page--cover">
  <svg class="cover-art" viewBox="0 0 387 501" preserveAspectRatio="none" aria-hidden="true">
    <defs>
      <linearGradient id="coverMist" x1="0" y1="0" x2="1" y2="1">
        <stop offset="0" stop-color="#ffffff"/>
        <stop offset="1" stop-color="#e6eaed"/>
      </linearGradient>
      <linearGradient id="bandShade" x1="0" y1="0" x2="0" y2="1">
        <stop offset="0" stop-color="#000" stop-opacity=".25"/>
        <stop offset="1" stop-color="#000" stop-opacity="0"/>
      </linearGradient>
    </defs>
    <rect width="387" height="501" fill="var(--navy)"/>
    <circle cx="20" cy="256" r="270" fill="var(--teal)"/>
    <circle cx="20" cy="256" r="260" fill="url(#coverMist)"/>
    <rect x="0" y="165" width="387" height="108" fill="#ffffff"/>
    <rect x="270" y="273" width="117" height="6" fill="url(#bandShade)"/>
  </svg>
  <div class="brand brand--cover"><span class="brand__dot"></span>ventora</div>
  <h1 class="cover-title">LEADERSHIP AND<br>FINANCIAL HEALTH</h1>
  <p class="cover-subtitle">OF PASTORS IN LEBANON</p>
  <div class="cover-rule"></div>
  <p class="cover-year">2025 FINDINGS</p>
  <p class="cover-byline">A REPORT BY VENTORA</p>
</section>

<!-- Executive summary -->
<section class="page page--summary">
  <div class="running-head">
    <span class="running-head__line"></span><span class="running-head__dot"></span>
    <span class="running-head__pill">LEADERSHIP AND FINANCIAL HEALTH OF PASTORS IN LEBANON</span>
    <span class="running-head__dot"></span><span class="running-head__line"></span>
  </div>
  <h2 class="section-title">EXECUTIVE SUMMARY</h2>
  <h3 class="subhead summary-purpose">Purpose, Scope &amp; Methodology</h3>
  <div class="summary-icon" role="img" aria-label="Icon of two hands holding up a target"></div>
  <p class="body-text summary-intro">In early 2025, Ventora conducted a field-based survey to assess the preparedness of Christian ministry leaders in Lebanon regarding two critical areas: (1) leadership succession and (2) financial management. The goal was to move beyond assumptions and gather tangible, data-driven insights that could inform strategic interventions and donor partnerships.</p>
  <p class="body-text summary-method">The study involved 26 face-to-face interviews with pastors and ministry leaders across Lebanon—both urban and rural—spanning Baptist, Nazarene, and Church of God traditions. The majority of respondents were lead pastors with a median age of 55 and an average of 20 years in ministry. Interviews were conducted in Arabic, translated into English, and analyzed by Ventora in partnership with Cedar Path, a ministry based in Beirut.</p>
  <div class="summary-findings">
    <h3 class="subhead">Key Findings: Succession Planning &amp; Ministry Continuity</h3>
    <ul class="findings-list">
      <li>While the majority (69%) of pastors interviewed report having a succession plan, less than one-third were able to share tangible information about the succession plan (e.g. who, what, when and how), raising concerns about the sustainability of churches and ministry to span across multiple generations.</li>
      <li>Many churches face a leadership pipeline problem, citing generational differences, emigration, or other macro-influences.</li>
      <li>Legacy matters deeply to pastors, but a lack of structured transition planning undermines ministry continuity.</li>
    </ul>
  </div>
  <div class="page-foot">
    <span class="page-foot__line page-foot__line--lead"></span>
    <span class="page-foot__brand"><span></span>ventora</span>
    <span class="page-foot__line"></span><span class="page-foot__dot"></span>
    <span class="page-foot__num">02</span>
    <span class="page-foot__dot"></span><span class="page-foot__line page-foot__line--tail"></span>
  </div>
</section>

<!-- Findings and call to action -->
<section class="page page--findings">
  <div class="running-head">
    <span class="running-head__line"></span><span class="running-head__dot"></span>
    <span class="running-head__pill">LEADERSHIP AND FINANCIAL HEALTH OF PASTORS IN LEBANON</span>
    <span class="running-head__dot"></span><span class="running-head__line"></span>
  </div>
  <div class="findings-money">
    <h3 class="subhead">Key Findings: Ministry &amp; Personal Financial Management</h3>
    <ul class="findings-list findings-list--tight">
      <li>The majority of pastors (73%) report significant financial stress, largely driven by: small church budgets (under $30,000 USD annually), facility rental costs, declining donor support, economic uncertainty</li>
      <li>While most churches have oversight committees and balance sheets, few have long-term planning tools or paid staff.</li>
      <li>Less than one in five pastors save consistently, and retirement readiness is virtually nonexistent.</li>
    </ul>
  </div>
  <div class="findings-training">
    <h3 class="subhead">Key Findings: Openness to Education &amp; Training</h3>
    <ul class="findings-list">
      <li>Pastors expressed widespread interest in receiving practical training in budgeting, saving, stewardship, and long-term planning.</li>
      <li>Many see financial literacy as part of their spiritual and leadership responsibility, especially in stewarding churches through economic hardship.</li>
    </ul>
  </div>
  <div class="action-band">
    <h2 class="action-band__title">CALL TO<br>ACTION</h2>
    <p class="body-text action-band__lede">The findings reveal both promise and peril. While many pastors are deeply committed and aware of succession needs, financial instability and poor saving habits threaten their ability to retire and therefore delegate leadership responsibility to the next generation. As a result, churches and ministries alike face an existential threat — risk becoming obsolete at the end of a leader’s “career” as a minister. However, the data also points to a high-leverage opportunity: pastors are eager to learn, adapt, and lead—if equipped with the right tools and support.</p>
    <p class="body-text action-band__invite">Ventora invites partners to review the findings in this study to better understand the current situation facing faithful church leaders in the Middle East. Together, let’s partner together by investing in leadership pipelines, financial literacy initiatives, and sustainability strategies that will empower church leaders in Lebanon and beyond.</p>
  </div>
  <div class="page-foot">
    <span class="page-foot__line page-foot__line--lead"></span>
    <span class="page-foot__brand"><span></span>ventora</span>
    <span class="page-foot__line"></span><span class="page-foot__dot"></span>
    <span class="page-foot__num">02</span>
    <span class="page-foot__dot"></span><span class="page-foot__line page-foot__line--tail"></span>
  </div>
</section>

<!-- Contact -->
<section class="page page--contact">
  <svg class="cover-art" viewBox="0 0 387 501" preserveAspectRatio="none" aria-hidden="true">
    <defs>
      <linearGradient id="contactMist" x1="0" y1="0" x2="1" y2="1">
        <stop offset="0" stop-color="#ffffff"/>
        <stop offset="1" stop-color="#e6eaed"/>
      </linearGradient>
      <linearGradient id="contactShade" x1="0" y1="0" x2="0" y2="1">
        <stop offset="0" stop-color="#000" stop-opacity=".25"/>
        <stop offset="1" stop-color="#000" stop-opacity="0"/>
      </linearGradient>
    </defs>
    <rect width="387" height="501" fill="var(--navy)"/>
    <circle cx="20" cy="256" r="270" fill="var(--teal)"/>
    <circle cx="20" cy="256" r="260" fill="url(#contactMist)"/>
    <rect x="0" y="170" width="387" height="109" fill="#ffffff"/>
    <rect x="270" y="279" width="117" height="6" fill="url(#contactShade)"/>
  </svg>
  <h2 class="contact-title">Contact Us</h2>
  <ul class="contact-list">
    <li>
      <svg viewBox="0 0 16 16" aria-hidden="true"><circle cx="8" cy="8" r="8" fill="var(--navy-text)"/><path d="M5.2 4.2l1.4-.3.8 1.9-.9.7c.5 1.1 1.3 1.9 2.3 2.4l.7-.9 1.9.8-.3 1.4c-3.3.2-6.1-2.6-5.9-6z" fill="#fff"/></svg>
      012-555-0148
    </li>
    <li>
      <svg viewBox="0 0 16 16" aria-hidden="true"><circle cx="8" cy="8" r="8" fill="var(--navy-text)"/><g fill="none" stroke="#fff" stroke-width=".9"><circle cx="8" cy="8" r="4.3"/><ellipse cx="8" cy="8" rx="1.9" ry="4.3"/><path d="M3.7 8h8.6M4.4 5.8h7.2M4.4 10.2h7.2"/></g></svg>
      www.ventora.org
    </li>
    <li>
      <svg viewBox="0 0 16 16" aria-hidden="true"><circle cx="8" cy="8" r="8" fill="var(--navy-text)"/><rect x="4" y="5.3" width="8" height="5.6" rx=".6" fill="none" stroke="#fff" stroke-width=".9"/><path d="M4.2 5.6L8 8.6l3.8-3" fill="none" stroke="#fff" stroke-width=".9"/></svg>
      hello@ventora.org
    </li>
  </ul>
  <div class="brand brand--contact"><span class="brand__dot"></span>ventora</div>
</section>

</body>
</html>
```